Business Card Design Project

Business card design using our logo, consistent with website branding (www.brightvane.com.au) and includes our services:

advertising|sales|events|production

Details Required:

Dorian Webb
Managing Director

P 1300 586 231
M 0404 827 659
F (02) 9613 2048
E dorian@brightvane.com.au
W www.brightvane.com.au

Will be printed on high quality card with rounded corners.

Quick turnaround required, on standby for any questions to assist with this.

Will upload logo and previous drafts we didn't think were the right fit.

Target Market(s)

Senior business decision-makers

Industry/Entity Type

Business

Requirements
Must have
• Editable template, so details can be updated for staff

Must be in print ready format - please see specs I have just uploaded

```html
<!DOCTYPE html>
<html lang="en">
<head>
<meta charset="utf-8">
<title>BrightVane – Business Card</title>
<link href="https://fonts.googleapis.com/css2?family=Open+Sans:wght@400;700&family=Questrial&display=swap" rel="stylesheet">
<style>
  :root {
    --backdrop: #e9e9e9;
    --card: #ffffff;
    --card-edge: #f1f1f1;
    --ink: #3a3a3a;
    --ink-soft: #555555;
    --accent-orange: #f26522;
    --accent-amber: #f7a823;
    --accent-blue: #1e9fd8;
    --panel-top: #3b3b3b;
    --panel-bottom: #151515;
    --panel-text: #e6e6e6;
  }
  * { box-sizing: border-box; margin: 0; padding: 0; }
  html, body { width: 1200px; height: 456px; overflow: hidden; }
  body {
    background: var(--backdrop);
    font-family: "Questrial", "Open Sans", sans-serif;
    color: var(--ink);
  }
  .sheet {
    position: relative;
    width: 1200px; height: 456px;
    display: flex; justify-content: center; align-items: center; gap: 28px;
  }
  .card {
    position: relative;
    width: 496px; height: 275px;
    border-radius: 18px;
    background: radial-gradient(ellipse at 50% 40%, var(--card) 55%, var(--card-edge) 100%);
    box-shadow: 0 2px 6px rgba(0,0,0,.12);
    overflow: hidden;
  }
  .brand {
    position: absolute;
    display: flex; align-items: center;
  }
  .brand__dot {
    border-radius: 50%;
    background: var(--accent-orange);
    flex: none;
  }
  .brand__name {
    font-family: "Questrial", sans-serif;
    color: var(--ink);
    letter-spacing: .5px;
  }
  .card--front .brand { left: 62px; top: 92px; gap: 18px; }
  .card--front .brand__dot { width: 74px; height: 74px; }
  .card--front .brand__name { font-size: 46px; }
  .services {
    position: absolute; left: 0; right: 0; bottom: 30px;
    text-align: center;
    font-size: 10.5px; letter-spacing: 4.2px;
    color: var(--ink-soft); text-transform: uppercase;
  }
  .card--back .brand { left: 38px; top: 112px; gap: 9px; }
  .card--back .brand__dot { width: 36px; height: 36px; }
  .card--back .brand__name { font-size: 22px; }
  .contact-panel {
    position: absolute; left: 265px; right: 0; top: 48px; height: 183px;
    border-radius: 14px 0 0 14px;
    background: linear-gradient(180deg, var(--panel-top), var(--panel-bottom));
    padding: 18px 0 0 18px;
    font-family: "Open Sans", sans-serif;
  }
  .person__name {
    font-weight: 700; font-size: 19px; color: var(--accent-orange);
    text-transform: uppercase; letter-spacing: .3px; line-height: 1.1;
  }
  .person__role { font-size: 11px; color: var(--accent-blue); margin-top: 3px; }
  .contact-list { list-style: none; margin-top: 26px; }
  .contact-list li {
    display: flex; align-items: center; gap: 7px;
    font-size: 11px; color: var(--panel-text); line-height: 15.5px;
  }
  .contact-list svg { width: 10px; height: 10px; fill: var(--panel-text); flex: none; }
</style>
</head>
<body>
<main class="sheet">
  <section class="card card--front" aria-label="Business card front">
    <div class="brand">
      <span class="brand__dot"></span>
      <span class="brand__name">BrightVane</span>
    </div>
    <p class="services">Advertising | Sales | Events | Production</p>
  </section>

  <section class="card card--back" aria-label="Business card back">
    <div class="brand">
      <span class="brand__dot"></span>
      <span class="brand__name">BrightVane</span>
    </div>
    <div class="contact-panel">
      <p class="person__name">Dorian Webb</p>
      <p class="person__role">Managing Director</p>
      <ul class="contact-list">
        <li><svg viewBox="0 0 10 10"><path d="M1 3c0-1 1-2 4-2s4 1 4 2v1H7V3H3v1H1zM2 5h6l1 4H1z"/></svg>1300 586 231</li>
        <li><svg viewBox="0 0 10 10"><rect x="3" y="0.5" width="4" height="9" rx="0.8"/></svg>0404 827 659</li>
        <li><svg viewBox="0 0 10 10"><rect x="2.5" y="0.5" width="5" height="3"/><rect x="0.5" y="4" width="9" height="4" rx="0.6"/><rect x="2.5" y="7" width="5" height="2.5"/></svg>(02) 9613 2048</li>
        <li><svg viewBox="0 0 10 10"><path d="M5 0.5a4.5 4.5 0 1 0 2.5 8.2l-.5-.8A3.5 3.5 0 1 1 8.5 5v.6c0 .5-.3.9-.8.9s-.7-.4-.7-.9V3h-1v.4A2 2 0 1 0 6.2 6.6c.3.5.8.9 1.5.9 1 0 1.8-.8 1.8-1.9V5A4.5 4.5 0 0 0 5 .5zm0 5.6a1.1 1.1 0 1 1 0-2.2 1.1 1.1 0 0 1 0 2.2z"/></svg>dorian@brightvane.com.au</li>
        <li><svg viewBox="0 0 10 10"><path d="M5 .5a4.5 4.5 0 1 0 0 9 4.5 4.5 0 0 0 0-9zm0 1a3.5 3.5 0 0 1 3.4 2.7H1.6A3.5 3.5 0 0 1 5 1.5zM1.6 5.8h6.8a3.5 3.5 0 0 1-6.8 0z"/></svg>www.brightvane.com.au</li>
      </ul>
    </div>
  </section>
</main>
</body>
</html>
```